Cozy Sprouts Business Cards

I need a business card for my new Company called Cozy Sprouts. We create handmade baby moccasins, headbands, t-shirts and more. I want some that will appeal to parents, and to go with the colors of my logo that I have attached. feel free to be creative. I would like my logo placed somewhere on the card.

Industry/Entity Type

Retail

Contact Information for Business Card

Cozy Sprouts
24816 Maplecrest D #5172
Irvine Ca 92738
Rosalind Vantrey Ceo
Info@Cozy-Sprouts.com
www.Cozy-Sprouts.com
Phone 9495817320

Requirements
Nice to have
• Logo included

```html
<!DOCTYPE html>
<html lang="en">
<head>
<meta charset="utf-8">
<title>Cozy Sprouts Business Cards</title>
<link rel="stylesheet" href="https://fonts.googleapis.com/css2?family=Open+Sans:wght@400;600&display=swap">
<style>
  :root {
    --page-bg: #ecebe8;
    --card-white: #ffffff;
    --card-white-edge: #f1f1f1;
    --card-black: #141212;
    --card-black-light: #2a2626;
    --accent: #e8916a;
    --accent-strong: #e07d52;
    --ink: #2b2b2b;
    --ink-soft: #7a7a7a;
    --light-text: #f4f4f4;
    --faint-mark: #3a3230;
  }
  * { margin: 0; padding: 0; box-sizing: border-box; }
  html, body {
    width: 1200px;
    height: 1023px;
    overflow: hidden;
    background: var(--page-bg);
    font-family: "Open Sans", sans-serif;
  }
  .sheet {
    width: 1200px;
    height: 1023px;
    display: flex;
    flex-direction: column;
    align-items: center;
    justify-content: center;
    gap: 60px;
  }
  .card {
    width: 700px;
    height: 400px;
    position: relative;
    overflow: hidden;
    box-shadow: 0 10px 30px rgba(0,0,0,0.18);
  }

  /* Front */
  .card-front {
    background: linear-gradient(135deg, var(--card-white) 0%, var(--card-white-edge) 100%);
  }
  .brand {
    position: absolute;
    top: 62px;
    right: 56px;
    display: flex;
    align-items: center;
    gap: 16px;
  }
  .brand-square {
    width: 34px;
    height: 34px;
    background: var(--accent);
  }
  .brand-name {
    font-size: 42px;
    font-weight: 400;
    color: var(--ink);
    letter-spacing: 0.5px;
  }
  .person {
    position: absolute;
    left: 56px;
    top: 150px;
  }
  .person-name {
    font-size: 24px;
    color: var(--accent);
    line-height: 1.2;
  }
  .person-role {
    font-size: 16px;
    color: var(--ink-soft);
    margin-top: 2px;
  }
  .address {
    position: absolute;
    left: 56px;
    top: 232px;
    font-size: 17px;
    color: var(--ink);
    line-height: 1.5;
  }
  .contacts {
    position: absolute;
    left: 56px;
    top: 292px;
    list-style: none;
    font-size: 16px;
    color: var(--ink);
    line-height: 1.55;
  }
  .contacts li { display: flex; align-items: center; gap: 9px; }
  .contacts svg { width: 13px; height: 13px; flex: none; }
  .accent-bar {
    position: absolute;
    left: 0;
    right: 0;
    bottom: 0;
    height: 16px;
    background: linear-gradient(90deg, var(--accent) 0%, var(--accent-strong) 100%);
  }

  /* Back */
  .card-back {
    background: linear-gradient(160deg, var(--card-black-light) 0%, var(--card-black) 60%);
  }
  .back-decor {
    position: absolute;
    left: 150px;
    top: 60px;
    width: 190px;
    height: 190px;
    background: var(--faint-mark);
    opacity: 0.7;
  }
  .back-brand {
    position: absolute;
    left: 190px;
    top: 170px;
    display: flex;
    align-items: center;
    gap: 16px;
  }
  .back-brand .brand-name { color: var(--light-text); font-size: 44px; }
  .back-brand .brand-square { background: var(--light-text); width: 36px; height: 36px; }
  .back-web {
    position: absolute;
    left: 192px;
    top: 240px;
    font-size: 17px;
    color: var(--accent);
    letter-spacing: 0.5px;
  }
</style>
</head>
<body>
<main class="sheet">
  <section class="card card-front" aria-label="Card front">
    <div class="brand">
      <span class="brand-square"></span>
      <span class="brand-name">Cozy Sprouts</span>
    </div>
    <div class="person">
      <p class="person-name">Rosalind Vantrey</p>
      <p class="person-role">Ceo</p>
    </div>
    <address class="address" style="font-style:normal">
      24816 Maplecrest D #5172<br>
      Irvine Ca 92738
    </address>
    <ul class="contacts">
      <li>
        <svg viewBox="0 0 13 13" aria-hidden="true"><rect width="13" height="13" rx="2" fill="#e8916a"/><path d="M4 3.2c.6 0 1 .9 1.2 1.5.1.4-.6.8-.5 1.1.3.8 1 1.5 1.8 1.8.3.1.7-.6 1.1-.5.6.2 1.5.6 1.5 1.2 0 .8-.8 1.3-1.5 1.2C5.6 9.2 3.8 7.4 3.5 5.4 3.4 4 3.4 3.2 4 3.2z" fill="#fff"/></svg>
        <span>9495817320</span>
      </li>
      <li>
        <svg viewBox="0 0 13 13" aria-hidden="true"><rect width="13" height="13" rx="2" fill="#e8916a"/><rect x="2.5" y="3.8" width="8" height="5.6" fill="none" stroke="#fff" stroke-width="1"/><path d="M2.5 3.8l4 3 4-3" fill="none" stroke="#fff" stroke-width="1"/></svg>
        <span>Info@Cozy-Sprouts.com</span>
      </li>
      <li>
        <svg viewBox="0 0 13 13" aria-hidden="true"><circle cx="6.5" cy="6.5" r="6.5" fill="#e8916a"/><circle cx="6.5" cy="6.5" r="3.8" fill="none" stroke="#fff" stroke-width="0.9"/><path d="M2.7 6.5h7.6M6.5 2.7c-1.6 2-1.6 5.6 0 7.6M6.5 2.7c1.6 2 1.6 5.6 0 7.6" fill="none" stroke="#fff" stroke-width="0.8"/></svg>
        <span>www.Cozy-Sprouts.com</span>
      </li>
    </ul>
    <div class="accent-bar"></div>
  </section>

  <section class="card card-back" aria-label="Card back">
    <div class="back-decor"></div>
    <div class="back-brand">
      <span class="brand-name">Cozy Sprouts</span>
      <span class="brand-square"></span>
    </div>
    <p class="back-web">www.Cozy-Sprouts.com</p>
  </section>
</main>
</body>
</html>
```